Online Psychology Practice needs business cards.

Online Psychology service needs business cards. Have own logo- please see uploaded. I have other file formats if you need (not sure one needed?)

Details for Business Card:
Fiona Kettlewood
Clinical Psychologist BPsych, BPsych (Hons), MPsych (Clin), MAPS
T: 0457260714 | F: 08 71526804
E: hello@harbourlightmindcarestudio.com.au
W: harbourlightmindcarestudio.com.au

Industry/Entity Type

Health

Contact Information for Business Card

Logo plus details above (couldn't write in this section)

```html
<!DOCTYPE html>
<html lang="en">
<head>
<meta charset="utf-8">
<title>Harbourlight Mindcare Studio – Business Cards</title>
<link href="https://fonts.googleapis.com/css2?family=Cinzel:wght@600;700&family=Arimo:wght@400;700&display=swap" rel="stylesheet">
<style>
  :root {
    --backdrop: #3b3b3d;
    --navy: #1b4f73;
    --deep-blue: #1a5b82;
    --deep-blue-dark: #144a6c;
    --teal: #0f88a7;
    --paper: #ffffff;
    --ink-light: #eaf5f9;
    --ink-soft: #cfe9f1;
  }
  * { box-sizing: border-box; margin: 0; padding: 0; }
  html, body {
    width: 1200px;
    height: 900px;
    overflow: hidden;
    background: var(--backdrop);
  }
  .sheet {
    width: 1200px;
    height: 900px;
    display: flex;
    align-items: center;
    justify-content: center;
    gap: 48px;
  }
  .card {
    width: 540px;
    height: 310px;
    border-radius: 22px;
    overflow: hidden;
    position: relative;
    box-shadow: 0 18px 40px rgba(0,0,0,0.35);
  }

  /* Front: details side */
  .card--front {
    background: var(--paper);
    display: flex;
    flex-direction: column;
  }
  .front__brand {
    height: 138px;
    display: flex;
    align-items: center;
    justify-content: center;
    gap: 14px;
  }
  .brand-name {
    font-family: "Cinzel", serif;
    font-weight: 700;
    color: var(--navy);
    text-align: center;
    line-height: 1.1;
  }
  .front__brand .brand-name { font-size: 27px; letter-spacing: 1px; }
  .front__brand .brand-name span { display: block; }
  .brand-dot {
    width: 16px; height: 16px;
    border-radius: 50%;
    background: var(--teal);
    flex: none;
  }
  .front__identity {
    background: var(--teal);
    height: 66px;
    display: flex;
    flex-direction: column;
    align-items: center;
    justify-content: center;
    gap: 4px;
  }
  .person-name {
    font-family: "Cinzel", serif;
    font-weight: 600;
    font-size: 25px;
    letter-spacing: 1.5px;
    color: var(--navy);
    text-transform: uppercase;
  }
  .person-title {
    font-family: "Arimo", sans-serif;
    font-size: 13.5px;
    color: var(--ink-light);
  }
  .front__contact {
    flex: 1;
    background: var(--deep-blue);
    display: flex;
    flex-direction: column;
    align-items: center;
    justify-content: center;
    gap: 6px;
    font-family: "Arimo", sans-serif;
    font-size: 14px;
    color: var(--ink-light);
  }
  .contact-line b { font-weight: 700; }

  /* Back: brand side */
  .card--back {
    background: linear-gradient(135deg, var(--deep-blue) 0%, var(--deep-blue-dark) 100%);
    display: flex;
    flex-direction: column;
    align-items: center;
    justify-content: center;
    gap: 18px;
  }
  .card--back .brand-dot {
    width: 22px; height: 22px;
    background: var(--paper);
  }
  .card--back .brand-name {
    color: var(--paper);
    font-size: 30px;
    letter-spacing: 1.5px;
  }
  .card--back .brand-name span { display: block; }
</style>
</head>
<body>
  <main class="sheet">
    <section class="card card--front" aria-label="Business card, details side">
      <div class="front__brand">
        <span class="brand-dot"></span>
        <p class="brand-name"><span>Harbourlight</span><span>Mindcare Studio</span></p>
      </div>
      <div class="front__identity">
        <h1 class="person-name">Fiona Kettlewood</h1>
        <p class="person-title">Clinical Psychologist BPsych, BPsych (Hons), MPsych (Clin), MAPS</p>
      </div>
      <div class="front__contact">
        <p class="contact-line"><b>P</b> : 0457260714 | <b>F</b> : 08 71526804</p>
        <p class="contact-line"><b>E</b> : hello@harbourlightmindcarestudio.com.au</p>
        <p class="contact-line"><b>W</b> : www.harbourlightmindcarestudio.com.au</p>
      </div>
    </section>

    <section class="card card--back" aria-label="Business card, brand side">
      <span class="brand-dot"></span>
      <p class="brand-name"><span>Harbourlight</span><span>Mindcare Studio</span></p>
    </section>
  </main>
</body>
</html>
```